New Menu Design Project

Rolling Skillet & Brunch Cottage is a Canadian Franchise Chain that currently has 60+ locations. We are looking for our menu to be modernized and redesigned to keep ahead of current trends
Attached you will find our current menu with photos from our various photoshoots, please use as per needed on the menu as we have some great shots of our products that we would like to showcase, especially our pancakes, waffles, French toast & crepes
Additionally you will find a Sample Menu of what we were thinking but we would like to see what other modern menu designs/creative freedom you can come up with
Please remove all beverages from this menu
Please see below link for all files: https://files.brunchvault-share.net/folders/7K22tpwqrzLmxc0DvA9hSfYbN4eRz3Qw1?usp=share_link

```html
<!DOCTYPE html>
<html lang="en">
<head>
<meta charset="utf-8">
<title>Rolling Skillet &amp; Brunch Cottage – Eggs, Hash &amp; Omelettes</title>
<link rel="stylesheet" href="https://fonts.googleapis.com/css2?family=Titan+One&family=Oswald:wght@500;600&family=Poppins:wght@400;500;600;700;800&display=swap">
<style>
:root{
  --yellow:#f7cd1f;
  --red:#c4221a;
  --wine:#8a1812;
  --wine-dark:#5e0f0b;
  --black:#0d0d0d;
  --white:#ffffff;
  --ink:#111111;
}
*{margin:0;padding:0;box-sizing:border-box}
html,body{width:933px;height:1200px;overflow:hidden;background:var(--black)}
body{font-family:"Poppins",Arial,sans-serif;position:relative}
.backdrop{position:absolute;inset:0;width:933px;height:1200px}
.section-title{position:absolute;display:flex;align-items:center;justify-content:center}
.section-title svg{position:absolute;inset:0;width:100%;height:100%}
.section-title h2{position:relative;font-family:"Titan One",Arial,sans-serif;font-weight:400;font-size:26px;letter-spacing:1.5px;text-transform:uppercase;text-shadow:2px 2px 0 rgba(0,0,0,.55)}
.title-benedict{left:30px;top:36px;width:296px;height:54px}
.title-benedict h2{color:var(--yellow)}
.title-hash{left:486px;top:36px;width:338px;height:56px}
.title-hash h2{color:var(--red);text-shadow:2px 2px 0 rgba(0,0,0,.35)}
.title-omelettes{left:290px;top:720px;width:352px;height:54px}
.title-omelettes h2{color:var(--red);text-shadow:2px 2px 0 rgba(0,0,0,.35)}

.intro{position:absolute;font-size:12.5px;line-height:18px;font-weight:500}
.intro-benedict{left:33px;top:104px;width:320px;color:var(--ink)}
.intro-hash{left:370px;top:106px;width:563px;text-align:center;color:var(--white)}
.intro-omelettes{left:0;top:780px;width:933px;text-align:center;color:var(--white)}

.benedict-list{position:absolute;left:33px;top:166px;width:316px;list-style:none;display:flex;flex-direction:column;gap:12px}
.benedict-item .row{display:flex;justify-content:space-between;font-weight:700;font-size:14px;line-height:18px;color:var(--red)}
.benedict-item p{font-size:10.8px;line-height:12.5px;font-weight:500;color:var(--ink)}

.menu-item{position:absolute}
.menu-item .row{display:flex;justify-content:space-between;font-weight:700;font-size:14.5px;line-height:18px}
.menu-item p{font-size:11px;line-height:13px;font-weight:500}
.hash .row{color:var(--yellow)}
.hash p{color:var(--white)}
.hash-left{left:400px;width:262px}
.hash-right{left:694px;width:206px}
.hash-right p{font-size:10.6px}

.omelette .row{color:var(--white)}
.omelette p{color:var(--yellow)}
.om-1{left:77px;width:250px}
.om-2{left:352px;width:262px}
.om-3{left:640px;width:250px}

.photo{position:absolute;left:178px;top:508px;width:570px;height:176px;border-radius:24px;border:5px solid var(--white);background:radial-gradient(ellipse at 30% 55%,#f4e9d8 0 18%,transparent 19%),radial-gradient(ellipse at 55% 40%,#f7f2e9 0 17%,transparent 18%),radial-gradient(ellipse at 80% 55%,#f7f2e9 0 16%,transparent 17%),linear-gradient(120deg,#f5b718,#f9d02c 45%,#f3a51a);box-shadow:0 4px 14px rgba(0,0,0,.35)}

.footer-notes{position:absolute;left:71px;top:1112px;display:flex;align-items:center;gap:14px;color:var(--white);font-family:"Oswald",Arial,sans-serif;font-weight:600;font-size:12px;line-height:13px;text-transform:uppercase}
.note{display:flex;align-items:center;gap:6px}
.note svg{flex:none}
.note-signature span{width:40px;font-size:10.5px;line-height:11px}
.note-flavour span{width:258px}
.note-spice span{width:250px}
.highlight{color:var(--yellow)}
.disclaimer{position:absolute;left:71px;top:1166px;width:760px;font-size:10.5px;line-height:12.5px;color:var(--white);font-weight:500}
.brand{position:absolute;left:812px;top:1116px;display:flex;align-items:center;gap:6px}
.brand-dot{width:30px;height:30px;border-radius:50%;background:var(--yellow);flex:none}
.brand-name{font-weight:700;font-size:9px;line-height:10.5px;color:var(--yellow);width:80px}
</style>
</head>
<body>

<svg class="backdrop" viewBox="0 0 933 1200" aria-hidden="true">
  <defs>
    <linearGradient id="band" x1="0" x2="1" y1="0" y2="0">
      <stop offset="0" stop-color="#2c2c2c"/>
      <stop offset=".5" stop-color="#ececec"/>
      <stop offset="1" stop-color="#2c2c2c"/>
    </linearGradient>
    <linearGradient id="wine" x1="0" x2="0" y1="0" y2="1">
      <stop offset="0" stop-color="#9a1c15"/>
      <stop offset="1" stop-color="#5e0f0b"/>
    </linearGradient>
  </defs>
  <rect width="933" height="1200" fill="var(--black)"/>
  <rect y="470" width="933" height="250" fill="url(#band)"/>
  <polygon fill="var(--black)" points="0,0 933,0 933,490 900,497 860,489 820,499 780,491 740,500 700,490 660,498 620,489 580,500 540,491 500,499 460,490 420,498 380,492 340,500 300,494 260,502 220,495 180,503 140,496 100,502 60,494 20,501 0,497"/>
  <polygon fill="var(--yellow)" points="0,0 368,0 372,30 366,60 374,95 367,130 371,170 365,210 373,250 368,290 374,330 366,370 372,410 367,450 371,492 340,500 300,494 260,502 220,495 180,503 140,496 100,502 60,494 20,501 0,497"/>
  <polygon fill="url(#wine)" points="0,700 30,692 70,702 110,694 150,703 190,693 230,701 270,692 310,702 350,694 390,703 430,693 470,701 510,692 550,702 590,694 630,703 670,693 710,701 750,692 790,702 830,694 870,703 905,693 933,699 933,1112 0,1112"/>
  <polygon fill="var(--black)" points="0,1106 35,1098 75,1108 115,1099 155,1107 195,1098 235,1108 275,1100 315,1108 355,1098 395,1107 435,1099 475,1108 515,1098 555,1107 595,1099 635,1108 675,1098 715,1107 755,1099 795,1108 835,1098 875,1107 910,1099 933,1104 933,1200 0,1200"/>
</svg>

<header class="section-title title-benedict">
  <svg viewBox="0 0 296 54" preserveAspectRatio="none" aria-hidden="true"><polygon fill="var(--red)" points="6,4 60,0 120,5 190,1 250,4 292,2 296,20 290,36 295,52 230,50 160,54 90,50 30,53 2,50 5,32 0,16"/></svg>
  <h2>Eggs Benedict</h2>
</header>
<p class="intro intro-benedict">Served with homefries, fresh fruit and topped with cheese garnish.</p>
<ul class="benedict-list">
  <li class="benedict-item"><div class="row"><span>Bacon Benedict (840 Cals)</span><span>$14.79</span></div></li>
  <li class="benedict-item"><div class="row"><span>Ham Benedict (700 Cals)</span><span>$14.79</span></div></li>
  <li class="benedict-item"><div class="row"><span>Peameal Benedict (820 Cals)</span><span>$14.79</span></div></li>
  <li class="benedict-item"><div class="row"><span>Turkey Bacon Benedict (750 Cals)</span><span>$14.79</span></div></li>
  <li class="benedict-item"><div class="row"><span>Peameal &amp; Spinach (820 Cals)</span><span>$15.79</span></div></li>
  <li class="benedict-item"><div class="row"><span>Spinach &amp; Mushroom (650 Cals)</span><span>$15.79</span></div></li>
  <li class="benedict-item"><div class="row"><span>Southwest Benedict<br>(720 Cals)</span><span>$15.79</span></div><p>Fresh guacamole and pico salsa topped with chipotle mayo and cheddar.</p></li>
  <li class="benedict-item"><div class="row"><span>Pulled Pork &amp; Mozza Benedict<br>(920 Cals)</span><span>$17.99</span></div><p>Marinated pulled pork topped with buffalo ranch and mozza.</p></li>
</ul>

<header class="section-title title-hash">
  <svg viewBox="0 0 338 56" preserveAspectRatio="none" aria-hidden="true"><polygon fill="var(--yellow)" points="4,6 70,1 140,5 210,0 280,4 334,2 338,22 332,40 337,54 260,52 190,56 110,51 40,55 2,52 6,34 0,18"/></svg>
  <h2>Stacked Hash’s</h2>
</header>
<p class="intro intro-hash">Topped with 2 eggs, tossed with homefries and served with Texas Toast.</p>

<article class="menu-item hash hash-left" style="top:138px"><div class="row"><span>Bacon Cheeseburger Hash<br>(1630 Cals)</span><span>$17.89</span></div><p>Ground beef, bacon, cheddar, caramelized onions and chipotle mayo.</p></article>
<article class="menu-item hash hash-left" style="top:210px"><div class="row"><span>Mexican Hash<br>(1060 Cals)</span><span>$16.79</span></div><p>Sausage, peppers, onions, mozza, buffalo sauce, guacamole and pico salsa.</p></article>
<article class="menu-item hash hash-left" style="top:286px"><div class="row"><span>Cowboy Hash<br>(1080 Cals)</span><span>$16.79</span></div><p>Bacon, ham, sausage, peppers, onions, cheddar and BBQ sauce.</p></article>
<article class="menu-item hash hash-left" style="top:362px"><div class="row"><span>Canadian Hash<br>(1260 Cals)</span><span>$16.79</span></div><p>Maple bacon, peameal, mushrooms and cheddar.</p></article>

<article class="menu-item hash hash-right" style="top:138px"><div class="row"><span>Benedict Hash<br>(1250 Cals)</span><span>$16.79</span></div><p>Peameal, cheddar, and hollandaise sauce.</p></article>
<article class="menu-item hash hash-right" style="top:211px"><div class="row"><span>Veggie Hash<br>(970 Cals)</span><span>$16.79</span></div><p>Mushrooms, tomatoes, onions, green peppers, spinach, served with guacamole and pico salsa.</p></article>
<article class="menu-item hash hash-right" style="top:314px"><div class="row"><span>Stacked Hash<br>(1120 Cals)</span><span>$17.89</span></div><p>Sautéed onions and green peppers topped with shaved corned beef, hollandaise and mozza.</p></article>
<article class="menu-item hash hash-right" style="top:408px"><div class="row"><span>Pulled Pork Hash<br>(1390 Cals)</span><span>$18.99</span></div><p>Marinated pulled pork, mozza, buffalo ranch, pico salsa and crispy onions.</p></article>

<div class="photo" role="img" aria-label="Overhead photo of pancakes, a fruit-topped waffle and French toast on white plates over a yellow table"></div>

<header class="section-title title-omelettes">
  <svg viewBox="0 0 352 54" preserveAspectRatio="none" aria-hidden="true"><polygon fill="var(--yellow)" points="5,5 80,0 150,4 230,1 300,5 348,2 352,22 346,38 351,52 270,50 190,54 110,50 40,54 2,50 6,32 0,16"/></svg>
  <h2>Stacked Omelettes</h2>
</header>
<p class="intro intro-omelettes">Served with homefries &amp; Texas toast. Substitute egg whites, add $1.99.</p>

<article class="menu-item omelette om-1" style="top:808px"><div class="row"><span>Western<br>(660 Cals)</span><span>$12.79</span></div><p>Ham and onions.</p></article>
<article class="menu-item omelette om-1" style="top:863px"><div class="row"><span>Deluxe Western<br>(850 Cals)</span><span>$13.89</span></div><p>Ham, onions, peppers and cheddar.</p></article>
<article class="menu-item omelette om-1" style="top:918px"><div class="row"><span>Vegetarian<br>(690 Cals)</span><span>$13.89</span></div><p>Mushrooms, peppers, onions and tomatoes.</p></article>
<article class="menu-item omelette om-1" style="top:974px"><div class="row"><span>Mexican<br>(930 Cals)</span><span>$14.99</span></div><p>Sausage, peppers, onions, mozza, buffalo sauce, guacamole and pico salsa.</p></article>

<article class="menu-item omelette om-2" style="top:808px"><div class="row"><span>Spinach Florentine<br>(920 Cals)</span><span>$14.99</span></div><p>Spinach, mushrooms, onions, mozza, topped with hollandaise and tomatoes.</p></article>
<article class="menu-item omelette om-2" style="top:877px"><div class="row"><span>Great Canadian<br>(880Cals)</span><span>$13.89</span></div><p>Bacon, mushrooms and cheddar.</p></article>
<article class="menu-item omelette om-2" style="top:933px"><div class="row"><span>Homestyle<br>(930 Cals)</span><span>$14.99</span></div><p>Bacon, ham, sausage, onions, peppers and cheddar.</p></article>
<article class="menu-item omelette om-2" style="top:1008px"><div class="row"><span>Greek<br>(780 Cals)</span><span>$13.89</span></div><p>Onions, tomatoes, peppers and feta.</p></article>

<article class="menu-item omelette om-3" style="top:808px"><div class="row"><span>Meatlovers<br>(930 Cals)</span><span>$13.89</span></div><p>Bacon, ham, sausage and cheddar.</p></article>
<article class="menu-item omelette om-3" style="top:863px"><div class="row"><span>Spinach<br>(790 Cals)</span><span>$14.99</span></div><p>Spinach, feta, tomatoes, mushrooms, peppers and onions.</p></article>
<article class="menu-item omelette om-3" style="top:933px"><div class="row"><span>Build Your Own<br>(665–990 Cals)</span><span>$14.99</span></div><p>3 eggs with your choice of 4 toppings: onions, green peppers, tomatoes, mushrooms, jalapeños, spinach, guacamole, pico salsa, bacon, ham, sausage, cheddar, mozza, feta or BBQ sauce.</p></article>

<footer>
  <div class="footer-notes">
    <div class="note note-signature">
      <svg width="34" height="30" viewBox="0 0 34 30" aria-hidden="true"><ellipse cx="17" cy="22" rx="15" ry="5" fill="none" stroke="var(--white)" stroke-width="2"/><ellipse cx="17" cy="15" rx="13" ry="4.5" fill="none" stroke="var(--white)" stroke-width="2"/><ellipse cx="17" cy="8" rx="11" ry="4" fill="none" stroke="var(--white)" stroke-width="2"/></svg>
      <span>Signature Item</span>
    </div>
    <div class="note note-flavour">
      <svg width="28" height="28" viewBox="0 0 24 24" aria-hidden="true"><polygon fill="var(--white)" points="12,1 15,9 23,9 16.5,14 19,22 12,17 5,22 7.5,14 1,9 9,9"/></svg>
      <span>Flavour your stack to any of the options under <span class="highlight">“Signature Stacks”</span> for $1.99 (235 - 1000 Cals)</span>
    </div>
    <div class="note note-spice">
      <svg width="30" height="26" viewBox="0 0 30 26" aria-hidden="true"><path d="M3 24 L10 3" stroke="var(--white)" stroke-width="3" stroke-linecap="round"/><text x="12" y="21" fill="var(--white)" font-family="Poppins, Arial, sans-serif" font-weight="800" font-size="13">HF</text></svg>
      <span>Spice up your homefries with sautéed onions, peppers and jalapeños for $1.99 (150 Cals)</span>
    </div>
  </div>
  <p class="disclaimer">Adults and youth (ages 13 and older) need an average of 2,000 calories a day, and children (ages 4 to 12) need an average of 1,500 calories a day. However, individual needs vary.</p>
  <div class="brand">
    <span class="brand-dot"></span>
    <span class="brand-name">Rolling Skillet &amp; Brunch Cottage</span>
  </div>
</footer>

</body>
</html>
```